Commercial Auto Insurance Application and Commercial Property Insurance Application

Hi I need a fillable application for my business to send to potential clients for Commercial Auto Insurance and Commercial Property Insurance. I have attached an example application I currently use for another line of insurance.
Commercial Auto Insurance Application
On the first page I would need the following:
- Business Name: (fill in area for text)
- Effective Date: (fill in area for text)
- How do you structure your business? (Check box for “Sole Proprietor”, “Partnership”, “Corporation”, “LLC”)
- Contact Name: (fill in area for text) / Phone Number: (fill in area for text) / Contact Email (fill in area for text)
- Mailing address: (fill in area for text)
- Garaging location: (fill in area for text)
- Owner Name: (fill in area for text)
- Description of Operations: (fill in area for text)
- How long has the operation been in business? (fill in area for text)
- How many years of experience does your management have in the truck/transportation industry? (fill in area for text)
Coverages
Liability Combined Single Limit: ($1,000,000 (checkbox) / $500,000 (checkbox / $300,000 (checkbox) / Other: (fill in area for text)
Uninsured Motorist CSL: (fill in area for text) (checkbox for “Rejected”)
Medical Payments: (fill in area for text)
Physical Damage: (fill in area for text) (checkbox for Rejected)
Liability Deducible: ($500 checkbox, $1,000 checkbox, $2,500 checkbox, $5,000 checkbox)
Physical Damage Deductible: ($500 checkbox, $1,000 checkbox, $2,500 checkbox, $5,000 checkbox)
Driving radius: (fill in area for text)
How many years have you had your own continuous commercial auto insurance coverage for the current business name? (fill in area for text)
Do any of your vehicles travel across state lines? Yes (checkbox)/ No (checkbox)
If yes, please list all states in which vehicles operate: (fill in area for text)
What is the maximum radius traveled for your customer's business?
0-25 miles (checkbox)
26-50 miles (checkbox)
51-75 miles (checkbox)
76-100 miles (checkbox)
101-150 miles (checkbox)
151-200 miles (checkbox)
201-300 miles (checkbox)
300+ miles (checkbox)
Would you like physical damage coverage for this vehicle? (should be for each vehicle listed)
On the 2nd page of the application I would need the following:
I would need to have it where people can fill in the vehicle information such as VIN:, Year:, Make:, Model:, Type of Vehicle:, Trailers:, Value:
I would also need to have it where people can fill in the drivers with their driver info including Name:, DOB:, DL #:, DL State:, Class of License:, Married: Yes/No, Number of years driving similar vehicle:
Please make it where you can fill in 20 vehicle's information and 20 driver's info.
For the 2nd Application I would need one for Property Insurance
On the Commercial Property Application I would need the following:
- Building Address: (fill in area for text)
- Building Description: (fill in area for text)
- Building Amount: $(fill in area for text)
- Business Personal Property Amount: $ (fill in area for text) (checkbox for Not Needed)
- Building Sq Ft: (fill in area for text)
- Total Area Sq Ft: (fill in area for text)
- Building Construction Type: Wood Frame (checkbox), Steel (checkbox), Fire Resistive (checkbox), Non-Combustible (checkbox), Other (fill in area for text)
- # of stories: (fill in area for text)
- Year Built: (fill in area for text)
- Wiring improvement year: (fill in area for text)
- Roofing improvement year: (fill in area for text)
- Plumbing improvement year: (fill in area for text)
- Heating improvement year: (fill in area for text)
- What is to the right of the building and distance: (fill in area for text)
- What is to the left of the building and distance: (fill in area for text)
- What is in front of the building and distance: (fill in area for text)
- What is behind the building and distance: (fill in area for text)
- Burglar alarm installation and serviced by: (fill in area for text) None (checkbox)
- Does the premises have fire protection? Sprinkler system (checkbox), Fire detection (checkbox), Other: (fill in area for text) None (checkbox)

```html
<!DOCTYPE html>
<html lang="en">
<head>
<meta charset="utf-8">
<title>Ridgeway Insurance Services – Application Forms</title>
<link href="https://fonts.googleapis.com/css2?family=Lato:wght@400;700;900&display=swap" rel="stylesheet">
<style>
  :root {
    --backdrop: #ffcc90;
    --paper: #ffffff;
    --navy: #27388a;
    --ink: #2d3a86;
    --field: #d4dcf0;
    --check: #3aa56b;
    --brand-green: #2fa84f;
    --frame: #4a4a4a;
    --veh-head: #a7a6cc;
    --veh-stripe: #dcdaee;
    --drv-head: #9fd6b1;
    --drv-stripe: #cfeadb;
    --grid: #7d7d99;
  }
  * { box-sizing: border-box; margin: 0; padding: 0; }
  html, body { width: 900px; height: 1200px; overflow: hidden; }
  body { font-family: "Lato", Arial, sans-serif; color: var(--ink); }
  .canvas { position: relative; width: 900px; height: 1200px; background: var(--backdrop); overflow: hidden; }

  .sheet { position: absolute; width: 391px; height: 553px; background: var(--paper); }
  .sheet--auto { left: 52px; top: 35px; }
  .sheet--schedule { left: 465px; top: 35px; }
  .sheet--property { left: 254px; top: 611px; }
  .sheet-frame { position: absolute; inset: 10px; border: 1px solid var(--frame); }

  .brand { position: absolute; left: 21px; top: 24px; display: flex; align-items: center; gap: 5px;
           font-weight: 900; font-size: 13px; color: var(--navy); letter-spacing: 0.3px; }
  .brand-mark { width: 9px; height: 9px; background: var(--brand-green); }
  .office { position: absolute; right: 21px; top: 24px; text-align: right; font-size: 5.4px; line-height: 7.2px; color: var(--navy); }
  .sheet-title { position: absolute; left: 0; right: 0; text-align: center; font-weight: 700; color: var(--navy); }
  .sheet--auto .sheet-title { top: 62px; font-size: 11.5px; }
  .sheet--property .sheet-title { top: 62px; font-size: 11px; }

  .field { background: var(--field); height: 10px; }
  .grow { flex: 1; }
  .box { display: inline-block; width: 8px; height: 8px; border: 1px solid var(--check); background: #fff; flex: none; }

  /* Auto application */
  .auto-form { position: absolute; left: 13px; right: 19px; top: 78px; font-size: 6.9px; font-weight: 700; }
  .row { display: flex; align-items: center; height: 15.7px; gap: 4px; white-space: nowrap; }
  .row.bullet::before { content: "•"; font-size: 8px; color: #222; margin-right: 1px; }
  .row.indent { padding-left: 6px; }
  .row .field { height: 10px; }
  .row .field.block { margin-left: 6px; }
  .radius-grid { display: grid; grid-template-columns: 73px 68px 67px auto; padding-left: 6px; }
  .radius-grid span { display: flex; align-items: center; gap: 5px; height: 15.7px; }
  .damage-notes { position: absolute; left: 19px; right: 19px; top: 473px; height: 59px;
                  background: var(--field); border-bottom-right-radius: 34px; border-top-right-radius: 0; }
  .page-badge { position: absolute; right: 19px; bottom: 15px; width: 31px; height: 21px; background: var(--navy);
                border-radius: 4px; color: #fff; font-size: 7px; font-weight: 700;
                display: flex; align-items: center; justify-content: flex-end; padding-right: 4px; }

  /* Schedule page */
  .table-title { position: absolute; left: 0; right: 0; text-align: center; font-size: 11px; font-weight: 700; color: var(--navy); }
  .table-title--vehicles { top: 21px; }
  .table-title--drivers { top: 272px; }
  .schedule { position: absolute; left: 30px; border-collapse: collapse; table-layout: fixed; font-size: 6.6px; font-weight: 700; color: #111; }
  .schedule th, .schedule td { border: 0.6px solid var(--grid); height: 10.3px; padding: 0; text-align: center; line-height: 9px; }
  .schedule--vehicles { top: 41px; width: 331px; }
  .schedule--vehicles th { background: var(--veh-head); }
  .schedule--vehicles tbody tr:nth-child(even) td { background: var(--veh-stripe); }
  .schedule--drivers { top: 297px; width: 343px; }
  .schedule--drivers th { background: var(--drv-head); }
  .schedule--drivers tbody tr:nth-child(even) td { background: var(--drv-stripe); }
  .schedule th.tiny { font-size: 4.2px; line-height: 4.5px; }
  .schedule th small { display: block; font-size: 2.6px; }

  /* Property application */
  .property-form { position: absolute; left: 21px; right: 25px; top: 80px; font-size: 8.3px; font-weight: 700; }
  .property-form .row { height: 19.7px; gap: 5px; }
  .property-form .field { height: 10px; }
</style>
</head>
<body>
<div class="canvas">

  <!-- Commercial auto application, page 1 -->
  <section class="sheet sheet--auto">
    <div class="sheet-frame"></div>
    <div class="brand"><span class="brand-mark"></span>RIDGEWAY</div>
    <address class="office">Ridgeway Insurance Services<br>4820 Meadow Crest Ave Suite 110<br>Fairview, CA 90000<br>Tel: (555) 014-2290</address>
    <h1 class="sheet-title">COMMERCIAL AUTO INSURANCE APPLICATION</h1>

    <div class="auto-form">
      <div class="row bullet">Business Name: <span class="field" style="width:148px"></span> - Effective Date: <span class="field grow"></span></div>
      <div class="row bullet">How do you structure your business? <span class="box"></span> Sole Proprietor <span class="box"></span> Partnership <span class="box"></span> Corporation &nbsp;&nbsp;<span class="box"></span> LLC</div>
      <div class="row bullet">Contact Name : <span class="field" style="width:70px"></span> / Phone Number : <span class="field" style="width:45px"></span> / Contact Email : <span class="field grow"></span></div>
      <div class="row bullet">Mailing address: <span class="field" style="width:114px"></span> - Garaging location: <span class="field grow"></span></div>
      <div class="row bullet">Owner Name: <span class="field" style="width:130px"></span> - Description of Operations: <span class="field grow"></span></div>
      <div class="row bullet">How long has the operation been in business? <span class="field grow"></span></div>
      <div class="row bullet">How many years of experience does your management have in the truck/transportation industry?</div>
      <div class="row"><span class="field block grow" style="height:15px"></span></div>
      <div class="row bullet">Coverages</div>
      <div class="row bullet">Liability Combined Single Limit: &nbsp;$1,000,000 <span class="box"></span> / $500,000 <span class="box"></span> &nbsp;/ $300,000 <span class="box"></span> / Other: <span class="field grow" style="margin-left:4px"></span></div>
      <div class="row bullet">Uninsured Motorist CSL: <span class="field grow"></span></div>
      <div class="row bullet">Medical Payments: <span class="field grow"></span></div>
      <div class="row bullet">Physical Damage: <span class="field grow"></span></div>
      <div class="row bullet">Liability Deducible: ( $500 <span class="box"></span> - $1,000 <span class="box"></span> - $2,500 <span class="box"></span> - $5,000 <span class="box"></span> )</div>
      <div class="row bullet">Physical Damage Deductible: ( $500 <span class="box"></span> - $1,000 <span class="box"></span> - $2,500 <span class="box"></span> - $5,000 <span class="box"></span> )</div>
      <div class="row bullet">Driving radius: <span class="field grow"></span></div>
      <div class="row bullet">How many years have you had your own continuous commercial auto insurance coverage for the current</div>
      <div class="row indent">business name? <span class="field grow"></span></div>
      <div class="row bullet">Do any of your vehicles travel across state lines? ( Yes <span class="box"></span> / No <span class="box"></span> )</div>
      <div class="row indent">If yes, please list all states in which vehicles operate:</div>
      <div class="row"><span class="field block grow" style="height:15px"></span></div>
      <div class="row bullet">What is the maximum radius traveled for your customer's business?</div>
      <div class="radius-grid">
        <span>0-25 miles <i class="box"></i></span>
        <span>26-50 miles <i class="box"></i></span>
        <span>51-75 miles <i class="box"></i></span>
        <span>76-100 miles <i class="box"></i></span>
        <span>101-150 miles <i class="box"></i></span>
        <span>151-200 miles <i class="box"></i></span>
        <span>201-300 miles <i class="box"></i></span>
        <span>300+ miles <i class="box"></i></span>
      </div>
      <div class="row bullet">Would you like physical damage coverage for this vehicle? (should be for each vehicle listed)</div>
    </div>
    <div class="damage-notes"></div>
    <div class="page-badge" role="img" aria-label="Delivery truck icon with page number 01">01</div>
  </section>

  <!-- Commercial auto application, page 2 -->
  <section class="sheet sheet--schedule">
    <div class="sheet-frame"></div>
    <h2 class="table-title table-title--vehicles">VEHICLE INFORMATION</h2>
    <table class="schedule schedule--vehicles">
      <thead><tr><th>Num</th><th>VIN</th><th>Year</th><th>Make</th><th>Model</th><th>Type</th><th>Trailers</th><th>Value</th></tr></thead>
      <tbody>
        <tr><td>01</td><td></td><td></td><td></td><td></td><td></td><td></td><td></td></tr>
        <tr><td>02</td><td></td><td></td><td></td><td></td><td></td><td></td><td></td></tr>
        <tr><td>03</td><td></td><td></td><td></td><td></td><td></td><td></td><td></td></tr>
        <tr><td>04</td><td></td><td></td><td></td><td></td><td></td><td></td><td></td></tr>
        <tr><td>05</td><td></td><td></td><td></td><td></td><td></td><td></td><td></td></tr>
        <tr><td>06</td><td></td><td></td><td></td><td></td><td></td><td></td><td></td></tr>
        <tr><td>07</td><td></td><td></td><td></td><td></td><td></td><td></td><td></td></tr>
        <tr><td>08</td><td></td><td></td><td></td><td></td><td></td><td></td><td></td></tr>
        <tr><td>09</td><td></td><td></td><td></td><td></td><td></td><td></td><td></td></tr>
        <tr><td>10</td><td></td><td></td><td></td><td></td><td></td><td></td><td></td></tr>
        <tr><td>11</td><td></td><td></td><td></td><td></td><td></td><td></td><td></td></tr>
        <tr><td>12</td><td></td><td></td><td></td><td></td><td></td><td></td><td></td></tr>
        <tr><td>13</td><td></td><td></td><td></td><td></td><td></td><td></td><td></td></tr>
        <tr><td>14</td><td></td><td></td><td></td><td></td><td></td><td></td><td></td></tr>
        <tr><td>15</td><td></td><td></td><td></td><td></td><td></td><td></td><td></td></tr>
        <tr><td>16</td><td></td><td></td><td></td><td></td><td></td><td></td><td></td></tr>
        <tr><td>17</td><td></td><td></td><td></td><td></td><td></td><td></td><td></td></tr>
        <tr><td>18</td><td></td><td></td><td></td><td></td><td></td><td></td><td></td></tr>
        <tr><td>19</td><td></td><td></td><td></td><td></td><td></td><td></td><td></td></tr>
        <tr><td>20</td><td></td><td></td><td></td><td></td><td></td><td></td><td></td></tr>
      </tbody>
    </table>

    <h2 class="table-title table-title--drivers">DRIVER INFORMATION</h2>
    <table class="schedule schedule--drivers">
      <colgroup><col style="width:41px"><col style="width:67px"><col style="width:28px"><col style="width:41px"><col style="width:41px"><col style="width:42px"><col style="width:41px"><col style="width:42px"></colgroup>
      <thead><tr><th>Num</th><th>Name</th><th>DOB</th><th>DL</th><th>DL State</th><th class="tiny">Class of License</th><th>Married</th><th class="tiny">Driving Yrs<small>Same Type</small></th></tr></thead>
      <tbody>
        <tr><td>01</td><td></td><td></td><td></td><td></td><td></td><td></td><td></td></tr>
        <tr><td>02</td><td></td><td></td><td></td><td></td><td></td><td></td><td></td></tr>
        <tr><td>03</td><td></td><td></td><td></td><td></td><td></td><td></td><td></td></tr>
        <tr><td>04</td><td></td><td></td><td></td><td></td><td></td><td></td><td></td></tr>
        <tr><td>05</td><td></td><td></td><td></td><td></td><td></td><td></td><td></td></tr>
        <tr><td>06</td><td></td><td></td><td></td><td></td><td></td><td></td><td></td></tr>
        <tr><td>07</td><td></td><td></td><td></td><td></td><td></td><td></td><td></td></tr>
        <tr><td>08</td><td></td><td></td><td></td><td></td><td></td><td></td><td></td></tr>
        <tr><td>09</td><td></td><td></td><td></td><td></td><td></td><td></td><td></td></tr>
        <tr><td>10</td><td></td><td></td><td></td><td></td><td></td><td></td><td></td></tr>
        <tr><td>11</td><td></td><td></td><td></td><td></td><td></td><td></td><td></td></tr>
        <tr><td>12</td><td></td><td></td><td></td><td></td><td></td><td></td><td></td></tr>
        <tr><td>13</td><td></td><td></td><td></td><td></td><td></td><td></td><td></td></tr>
        <tr><td>14</td><td></td><td></td><td></td><td></td><td></td><td></td><td></td></tr>
        <tr><td>15</td><td></td><td></td><td></td><td></td><td></td><td></td><td></td></tr>
        <tr><td>16</td><td></td><td></td><td></td><td></td><td></td><td></td><td></td></tr>
        <tr><td>17</td><td></td><td></td><td></td><td></td><td></td><td></td><td></td></tr>
        <tr><td>18</td><td></td><td></td><td></td><td></td><td></td><td></td><td></td></tr>
        <tr><td>19</td><td></td><td></td><td></td><td></td><td></td><td></td><td></td></tr>
        <tr><td>20</td><td></td><td></td><td></td><td></td><td></td><td></td><td></td></tr>
      </tbody>
    </table>
    <div class="page-badge" role="img" aria-label="Delivery truck icon with page number 02">02</div>
  </section>

  <!-- Property insurance application -->
  <section class="sheet sheet--property">
    <div class="sheet-frame"></div>
    <div class="brand"><span class="brand-mark"></span>RIDGEWAY</div>
    <address class="office">Ridgeway Insurance Services<br>4820 Meadow Crest Ave Suite 110<br>Fairview, CA 90000<br>Tel: (555) 014-2290</address>
    <h1 class="sheet-title">PROPERTY INSURANCE</h1>

    <div class="property-form">
      <div class="row">- Business Name: <span class="field" style="width:149px"></span></div>
      <div class="row">- Building Address: <span class="field grow"></span></div>
      <div class="row">- Building Description: <span class="field grow"></span></div>
      <div class="row">- Building Amount: $ <span class="field grow"></span></div>
      <div class="row">- Business Personal Property Amount: $ <span class="field" style="width:55px"></span> &nbsp;( &nbsp;<span class="box"></span> Not Needed )</div>
      <div class="row">- Building Sq Ft: <span class="field grow"></span></div>
      <div class="row">- Total Area Sq Ft: <span class="field grow"></span></div>
      <div class="row">- Building Construction Type: &nbsp;Wood Frame <span class="box"></span> &nbsp;&nbsp;- Steel &nbsp;&nbsp;&nbsp;&nbsp;&nbsp;<span class="box"></span> &nbsp;&nbsp;&nbsp;- Fire Resistive <span class="box"></span></div>
      <div class="row">Non-Combustible <span class="box"></span> - Other <span class="field grow"></span></div>
      <div class="row">- # of stories: <span class="field grow"></span></div>
      <div class="row">- Year Built: <span class="field grow"></span></div>
      <div class="row">- Wiring improvement year: <span class="field grow"></span></div>
      <div class="row">- Roofing improvement year: <span class="field grow"></span></div>
      <div class="row">- Plumbing improvement year: <span class="field grow"></span></div>
      <div class="row">- Heating improvement year: <span class="field grow"></span></div>
      <div class="row">- What is to the right of the building and distance: <span class="field grow"></span></div>
      <div class="row">- What is to the left of the building and distance: <span class="field grow"></span></div>
      <div class="row">- What is in front of the building and distance: <span class="field grow"></span></div>
      <div class="row">- What is behind the building and distance: <span class="field grow"></span></div>
      <div class="row">- Burglar alarm installation and serviced by: <span class="field" style="width:112px"></span> &nbsp;None <span class="box"></span></div>
      <div class="row">- Does the premises have fire protection?</div>
      <div class="row">&nbsp;Sprinkler system <span class="box"></span><span style="width:30px"></span>Fire detection <span class="box"></span><span style="width:42px"></span>None <span class="box"></span></div>
      <div class="row">Other: <span class="field grow"></span></div>
    </div>
  </section>

</div>
</body>
</html>
```